Flyer for a marketing

We are a holistic mental health facility in need of a flyer to help promote our services and encourage more people to seek care. See the attachment to tell you more. We prefer warm green colors or rich blue. Thank you.

```html
<!DOCTYPE html>
<html lang="en">
<head>
<meta charset="utf-8">
<title>Evergreen Mind Health and Wellness – Flyer</title>
<link rel="stylesheet" href="https://fonts.googleapis.com/css2?family=Arvo:wght@400;700&family=Montserrat:wght@400;500;600;800&display=swap">
<style>
  :root{
    --stage:#8a8a8a;
    --navy:#1b3a6b;
    --navy-deep:#193e75;
    --sky-blue:#33bde9;
    --accent-blue:#2fa8df;
    --white:#ffffff;
    --sky-top:#5f7294;
    --sky-mauve:#a98886;
    --sunset-orange:#e5842e;
    --sun-yellow:#f7c43c;
    --grass:#7fb43c;
    --rule:#3a5a8c;
  }
  *{box-sizing:border-box;margin:0;padding:0}
  html,body{width:668px;height:1200px;overflow:hidden;background:var(--stage)}
  .flyer{position:absolute;left:14px;top:151px;width:640px;height:898px;background:var(--white);overflow:hidden;font-family:'Montserrat',sans-serif;box-shadow:0 6px 18px rgba(0,0,0,.35)}
  .hero{position:absolute;left:0;top:0;width:640px;height:525px;
    background:
      radial-gradient(circle at 94% 92%, rgba(255,248,200,.95) 0, rgba(250,210,80,.8) 60px, rgba(247,196,60,0) 200px),
      linear-gradient(180deg,var(--sky-top) 0%,#7e7f98 22%,var(--sky-mauve) 42%,#d48c52 62%,var(--sunset-orange) 78%,#c9682a 100%)}
  .brand{position:absolute;left:34px;top:34px;color:var(--white)}
  .brand-row{display:flex;align-items:center;gap:14px}
  .brand-dot{width:30px;height:30px;border-radius:50%;background:var(--white);flex:none}
  .brand-name{font-family:'Arvo',serif;font-weight:700;font-size:16px;line-height:19px;border-left:1.5px solid var(--white);padding-left:12px}
  .brand-tag{font-size:11px;margin-top:10px;margin-left:14px}
  .photo{position:absolute;border:3px solid var(--white);border-radius:26px;box-shadow:0 3px 8px rgba(0,0,0,.3)}
  .photo-family{left:290px;top:30px;width:180px;height:170px;background:linear-gradient(135deg,#6f8a5a,#c9a98c 55%,#4c6a8a)}
  .photo-child{left:140px;top:208px;width:220px;height:150px;background:linear-gradient(135deg,#d8b98a,#2f4f8c 60%,#e8e4d8)}
  .photo-park{left:380px;top:208px;width:220px;height:150px;background:linear-gradient(135deg,#5d8a3a,#a9c46a 50%,#c8a24c)}
  .headline{position:absolute;left:0;width:640px;top:372px;text-align:center;font-family:'Arvo',serif;font-weight:700;color:var(--white);font-size:66px;line-height:64px;letter-spacing:-1px;
    -webkit-text-stroke:2px var(--navy);paint-order:stroke fill;text-shadow:0 3px 5px rgba(0,0,0,.3)}
  .band{position:absolute;left:0;top:525px;width:640px;height:44px;background:var(--sky-blue);color:var(--navy);font-weight:600;font-size:14px;line-height:18px;text-align:center;padding-top:4px}
  .grass{position:absolute;left:0;top:730px;width:640px;height:100px;background:linear-gradient(180deg,rgba(255,255,255,1) 0%,rgba(200,226,150,.7) 45%,var(--grass) 100%)}
  .why{position:absolute;left:34px;top:594px;width:270px}
  .why h2{font-family:'Arvo',serif;font-weight:700;font-size:26px;color:var(--accent-blue);margin-bottom:10px}
  .why ul{list-style:none}
  .why li{position:relative;padding:3px 0 4px 22px;font-size:9.5px;line-height:11px;color:var(--navy);border-bottom:1px dashed var(--rule)}
  .why li:last-child{border-bottom:none}
  .why li svg{position:absolute;left:0;top:5px}
  .divider{position:absolute;left:320px;top:590px;width:1px;height:225px;background:var(--navy)}
  .accepting{position:absolute;left:340px;top:588px;width:285px}
  .accepting h3{font-weight:800;font-size:17.5px;line-height:19px;color:var(--navy-deep)}
  .accepting p{font-size:10.8px;line-height:14px;color:var(--navy);margin-top:10px}
  .team{position:absolute;left:340px;top:694px;width:271px;height:119px;border:2px solid var(--sky-blue);border-radius:12px;background:linear-gradient(90deg,#f2e6e0,#7aa0cf 50%,#f4e2e8)}
  .footer{position:absolute;left:0;top:825px;width:640px;height:73px;background:var(--sky-blue)}
  .footer svg.shape{position:absolute;left:0;top:0}
  .address{position:absolute;left:34px;top:9px;color:var(--white)}
  .address .name{font-family:'Arvo',serif;font-weight:400;font-size:11.5px;color:var(--sky-blue);padding-left:18px;position:relative}
  .address .street{font-size:9px;padding-left:18px;margin-top:3px}
  .address .links{font-size:9.5px;margin-top:9px;display:flex;gap:10px}
  .address .links span{padding-left:17px;position:relative}
  .icon{position:absolute;left:0;top:1px}
  .contact{position:absolute;right:30px;top:14px;color:var(--white);font-size:15px;line-height:23px}
  .contact div{position:relative;padding-left:26px}
  .contact b{font-weight:800}
</style>
</head>
<body>
<main class="flyer">
  <section class="hero" role="img" aria-label="Sunset sky over a field, warm orange and golden light">
    <div class="brand">
      <div class="brand-row">
        <span class="brand-dot"></span>
        <div class="brand-name">Evergreen<br>Mind<br>Health<br>and<br>Wellness</div>
      </div>
      <div class="brand-tag">A Professional Nursing Corporation</div>
    </div>
    <div class="photo photo-family" role="img" aria-label="Photo: grandfather pouring a warm drink for a girl outdoors"></div>
    <div class="photo photo-child" role="img" aria-label="Photo: stressed boy holding his head over homework"></div>
    <div class="photo photo-park" role="img" aria-label="Photo: family playing together in a green park"></div>
    <h1 class="headline">The Care You<br>Deserve</h1>
  </section>

  <div class="band">Evergreen Mind Health and Wellness,<br>where deserving patients meet compassionate providers.</div>

  <div class="grass" role="img" aria-label="Green grass field fading into white"></div>

  <section class="why">
    <h2>Why choose us?</h2>
    <ul>
      <li><svg width="11" height="11" viewBox="0 0 11 11"><circle cx="5.5" cy="5.5" r="5.5" fill="#1b3a6b"/><path d="M3 5.7l1.7 1.6L8 4" stroke="#fff" stroke-width="1.3" fill="none"/></svg>We are an integrative<br>holistic psychiatric center.</li>
      <li><svg width="11" height="11" viewBox="0 0 11 11"><circle cx="5.5" cy="5.5" r="5.5" fill="#1b3a6b"/><path d="M3 5.7l1.7 1.6L8 4" stroke="#fff" stroke-width="1.3" fill="none"/></svg>Our mission is to provide compassionate<br>quality care.</li>
      <li><svg width="11" height="11" viewBox="0 0 11 11"><circle cx="5.5" cy="5.5" r="5.5" fill="#1b3a6b"/><path d="M3 5.7l1.7 1.6L8 4" stroke="#fff" stroke-width="1.3" fill="none"/></svg>We provide psychiatric services including<br>medication management and<br>psychotherapy.</li>
      <li><svg width="11" height="11" viewBox="0 0 11 11"><circle cx="5.5" cy="5.5" r="5.5" fill="#1b3a6b"/><path d="M3 5.7l1.7 1.6L8 4" stroke="#fff" stroke-width="1.3" fill="none"/></svg>We listen, care, and empower you to<br>live better.</li>
      <li><svg width="11" height="11" viewBox="0 0 11 11"><circle cx="5.5" cy="5.5" r="5.5" fill="#1b3a6b"/><path d="M3 5.7l1.7 1.6L8 4" stroke="#fff" stroke-width="1.3" fill="none"/></svg>We accept major insurances.</li>
    </ul>
  </section>

  <div class="divider"></div>

  <section class="accepting">
    <h3>WE ARE Accepting New<br>Patients, No waiting list.</h3>
    <p>Your mental health matters, so make it a<br>priority and call us today for an appointment.</p>
  </section>
  <div class="team" role="img" aria-label="Photo: smiling team of nurses and care providers"></div>

  <footer class="footer">
    <svg class="shape" width="640" height="73" viewBox="0 0 640 73"><path d="M0 0H300C370 2 390 40 412 73H0Z" fill="#193e75"/></svg>
    <div class="address">
      <div class="name"><svg class="icon" width="9" height="12" viewBox="0 0 9 12"><path d="M4.5 0A4.5 4.5 0 0 0 0 4.5C0 8 4.5 12 4.5 12S9 8 9 4.5A4.5 4.5 0 0 0 4.5 0Z" fill="#fff"/><circle cx="4.5" cy="4.5" r="1.7" fill="#193e75"/></svg>Evergreen Mind Health and Wellness, APNC</div>
      <div class="street">1480 Meadowbrook Lane, Suite 300 Fairview, CA 90210</div>
      <div class="links">
        <span><svg class="icon" width="10" height="8" viewBox="0 0 10 8"><rect width="10" height="8" fill="#fff"/><path d="M0 0l5 4 5-4" stroke="#193e75" fill="none"/></svg>info@evergreenmindhealth.com</span>
        <span><svg class="icon" width="10" height="10" viewBox="0 0 10 10"><circle cx="5" cy="5" r="4.3" stroke="#fff" fill="none"/><ellipse cx="5" cy="5" rx="1.8" ry="4.3" stroke="#fff" fill="none"/><path d="M.7 5h8.6" stroke="#fff"/></svg>evergreenmindhealth.com</span>
      </div>
    </div>
    <div class="contact">
      <div><svg class="icon" style="top:4px" width="14" height="14" viewBox="0 0 14 14"><path d="M3 1l2.5 3-1.5 1.5c.8 1.8 2.2 3.2 4 4L9.5 8l3 2.5L11 13C6 13 1 8 1 3Z" fill="#1b3a6b"/></svg>Ph <b>(555) 214-7730</b></div>
      <div><svg class="icon" style="top:4px" width="15" height="14" viewBox="0 0 15 14"><rect x="3" y="0" width="9" height="4" fill="#1b3a6b"/><rect x="0" y="4" width="15" height="7" rx="1.5" fill="#1b3a6b"/><rect x="3" y="8" width="9" height="6" fill="#1b3a6b" stroke="#33bde9"/></svg>Fax <b>(555) 214-7731</b></div>
    </div>
  </footer>
</main>
</body>
</html>
```